Wordpress coded website (5 page-home page, contact form & 3 common pages) for Skiing event

I would like a WordPress site designed for our Ski & Snowboard event. The site is to have 5 total pages.

Hosting has been setup (Bright Hostwell) and WordPress installed.

Requirements:
Front page with Landscape slide, Friendbook feed, 4 menu items, footer and small description section.

3 Separate pages to be created, with a similar layout with landscape image slider and large text section (content provided)

1 Contact us page with the below form sections
- Name
- School
- Position
- Email
- Phone
- Message

Target Market(s)

School teachers and school students

Industry/Entity Type

Tourism

Number of Pages Required

5+ page

Colors

Designer to choose colors to be used in the design.

Requirements
Must have
• Must include event logo attached in brief. Must include Friendbook feed on homepage

```html
<!DOCTYPE html>
<html lang="en">
<head>
<meta charset="utf-8">
<title>Snowline SKI Challenge</title>
<link rel="stylesheet" href="https://fonts.googleapis.com/css2?family=Lato:wght@400;700&display=swap">
<style>
:root{
  --blue:#0a93e0;
  --dark:#1f1f1f;
  --darker:#111;
  --ink:#222;
  --text:#333;
  --fb:#3b5998;
  --line:#d9d9d9;
  --white:#fff;
  --hero-a:#dfe4e8;
  --hero-b:#b9c0c5;
}
*{box-sizing:border-box;margin:0;padding:0}
html,body{width:1017px;height:1200px;overflow:hidden;background:var(--white);font-family:'Lato',sans-serif;color:var(--text)}
svg{flex:none}
.page{position:relative;width:1017px;height:1200px}
.top-contact{position:absolute;top:0;left:515px;height:30px;display:flex}
.top-contact .pill{display:flex;align-items:center;gap:8px;color:var(--white);font-size:13.5px;padding:0 14px 0 20px;height:30px;white-space:nowrap}
.pill.email{background:var(--ink);clip-path:polygon(0 0,100% 0,100% 100%,12px 100%);width:275px}
.pill.phone{background:var(--blue);clip-path:polygon(0 0,100% 0,calc(100% - 12px) 100%,0 100%);width:150px;padding-left:14px}
.pill .dot{width:19px;height:19px;border-radius:50%;background:var(--white);display:flex;align-items:center;justify-content:center;flex:none}
.brand-panel{position:absolute;left:83px;top:0;width:149px;height:175px;background:var(--white);box-shadow:0 2px 6px rgba(0,0,0,.12);clip-path:polygon(0 0,100% 0,100% 150px,50% 175px,0 150px);z-index:3;display:flex;align-items:center;justify-content:center;text-align:center}
.brand-name{color:var(--blue);font-weight:700;font-size:19px;line-height:1.15}
.nav{position:absolute;top:62px;left:400px;width:535px;display:flex;justify-content:space-between;align-items:center}
.nav a{font-size:15px;color:var(--ink);text-decoration:none}
.nav a.active{color:var(--blue);font-weight:700}
.nav .sep{width:1px;height:16px;background:var(--line)}
.nav-mark{position:absolute;left:432px;top:88px;width:14px;height:14px;border-radius:50%;background:var(--blue)}
.hero{position:absolute;top:113px;left:0;width:1017px;height:462px;background:linear-gradient(180deg,var(--hero-a),var(--hero-b))}
.hero-arrow{position:absolute;top:217px;width:36px;height:36px;background:rgba(30,30,30,.85);display:flex;align-items:center;justify-content:center}
.hero-arrow.prev{left:26px}.hero-arrow.next{right:26px}
.hero-title{position:absolute;bottom:22px;width:100%;text-align:center;color:var(--white);font-weight:700;font-size:34px;text-shadow:0 1px 4px rgba(0,0,0,.45)}
.about{position:absolute;left:84px;top:612px;width:590px}
.about h1{color:var(--blue);font-size:28px;font-weight:700}
.divider{display:flex;align-items:center;margin:18px 0 22px;gap:12px}
.divider .mark{width:18px;height:18px;border-radius:50%;background:#ccc}
.divider .rule{flex:1;height:2px;background:#e8e8e8}
.about .date{font-weight:700;font-size:13px;color:var(--ink);margin-bottom:2px}
.about p{font-size:12.8px;line-height:23.6px}
.about .note{margin-top:5px}
.feed{position:absolute;left:711px;top:619px;width:222px;height:249px;border:2px solid var(--fb)}
.feed-head{height:32px;background:var(--fb);color:var(--white);display:flex;justify-content:space-between;align-items:center;padding:0 12px;font-size:11.5px}
.feed-head b{font-weight:700;font-size:12px}
.feed-item{display:flex;gap:8px;margin:0 10px;padding:10px 0 8px;border-bottom:1px dotted #ccc}
.feed-thumb{width:44px;height:36px;flex:none;background:#9aa4ad}
.feed-item .t{color:var(--fb);font-size:10px;line-height:14.5px}
.feed-item .r{font-size:8px;color:var(--ink);margin-top:3px}
.feed-foot{position:absolute;bottom:0;left:0;right:0;border-top:1px solid #ddd;font-size:10px;color:#555;padding:8px 10px}
.footer{position:absolute;top:912px;left:0;width:1017px;height:251px;background:var(--dark);color:var(--white)}
.fcol{position:absolute;top:30px}
.fcol h3{font-size:17px;font-weight:700;padding-bottom:8px;border-bottom:1px solid #444;position:relative}
.fcol h3 span{color:var(--blue)}
.fcol h3::after{content:"";position:absolute;left:0;bottom:-1px;width:24px;height:1px;background:#888}
.vsep{position:absolute;top:40px;width:1px;height:180px;background:#333}
.links{list-style:none;margin-top:10px}
.links li{font-size:13px;line-height:30px}
.links li::before{content:"•";font-size:9px;margin-right:6px;vertical-align:middle}
.contact .name{font-weight:700;font-size:14px;margin-top:11px}
.contact .addr{font-size:11px;line-height:17px}
.contact .row{display:flex;align-items:center;gap:10px;font-size:11.5px;margin-top:14px;white-space:nowrap}
.form{margin-top:12px;display:flex;flex-direction:column;gap:6px}
.form .field{border:1px solid #3a3a3a;background:#1a1a1a;height:29px;font-size:11px;padding:8px 10px;color:#ddd}
.form .field.msg{height:36px}
.form .submit{width:87px;height:29px;background:var(--blue);color:var(--white);font-weight:700;font-size:13px;display:flex;align-items:center;justify-content:center;margin-top:2px}
.footer-brand{position:absolute;left:790px;top:50px;width:145px;height:150px;display:flex;align-items:center;justify-content:center;text-align:center;color:#9a9a9a;font-weight:700;font-size:21px;line-height:1.15}
.bottom{position:absolute;top:1163px;left:0;width:1017px;height:37px;background:var(--darker);color:var(--white);display:flex;align-items:center;justify-content:space-between;padding:0 83px 0 85px;font-size:11.5px}
.social{display:flex;gap:7px}
.social i{width:20px;height:20px;border-radius:50%;background:var(--white);display:block}
</style>
</head>
<body>
<div class="page">
  <div class="top-contact">
    <div class="pill email"><span class="dot"><svg width="10" height="8" viewBox="0 0 10 8"><rect x=".5" y=".5" width="9" height="7" fill="none" stroke="#222"/><path d="M.5 .5 5 4.5 9.5 .5" fill="none" stroke="#222"/></svg></span>enquiry@snowlineskichallenge.com.au</div>
    <div class="pill phone"><span class="dot"><svg width="10" height="8" viewBox="0 0 10 8"><rect x=".5" y=".5" width="9" height="7" fill="none" stroke="#0a93e0"/><path d="M.5 .5 5 4.5 9.5 .5" fill="none" stroke="#0a93e0"/></svg></span>02 5550 1842</div>
  </div>

  <div class="brand-panel"><div class="brand-name">Snowline<br>SKI<br>Challenge</div></div>

  <nav class="nav">
    <a class="active">Home</a><span class="sep"></span>
    <a>Event</a><span class="sep"></span>
    <a>Mt Corrie</a><span class="sep"></span>
    <a>Itinerary</a><span class="sep"></span>
    <a>Contact Us</a>
  </nav>
  <span class="nav-mark"></span>

  <section class="hero" role="img" aria-label="Slider photo: skis lying in fresh snow">
    <div class="hero-arrow prev"><svg width="10" height="14" viewBox="0 0 10 14"><path d="M8 1 2 7l6 6" fill="none" stroke="#fff" stroke-width="2"/></svg></div>
    <div class="hero-arrow next"><svg width="10" height="14" viewBox="0 0 10 14"><path d="M2 1l6 6-6 6" fill="none" stroke="#fff" stroke-width="2"/></svg></div>
    <h2 class="hero-title">Welcome To About Snowline SKI Challenge</h2>
  </section>

  <section class="about">
    <h1>About Snowline SKI Challenge</h1>
    <div class="divider"><span class="mark"></span><span class="rule"></span></div>
    <p class="date">Wednesday 11th July &amp; Thursday 12th July 2018.</p>
    <p>The Mt Corrie Ski Challenge is the first event of its kind in the Southern Hemisphere offering high school students from Australia to face off against New Zealand locals on the ski fields of Mt Corrie. With no race experience necessary, the event provides a great fun experience for those enjoying their first time on the slopes as well as providing a chance for experienced skiers and snowboarders to test themselves against the clock and other competitors.</p>
    <p class="note"><b>Notes:</b> No experience necessary badge to appear on page</p>
  </section>

  <aside class="feed">
    <div class="feed-head"><span>Recent Activity</span><b>Friendbook</b></div>
    <div class="feed-item"><div class="feed-thumb" role="img" aria-label="Thumbnail photo of a lodge"></div><div><div class="t">Lorem ipsum dolor sit amet the consectetuer adipi.</div><div class="r">2 people recommended this.</div></div></div>
    <div class="feed-item"><div class="feed-thumb" role="img" aria-label="Thumbnail photo of skis"></div><div><div class="t">Lorem ipsum dolor sit amet the adipiscing elit, sed di nonummy</div><div class="r">3 people recommended this.</div></div></div>
    <div class="feed-item" style="border:0"><div class="feed-thumb" role="img" aria-label="Thumbnail photo of ski boots"></div><div><div class="t">Lorem ipsum dolor sit amet the consectetuer adipiscing.</div><div class="r">2 people recommended this.</div></div></div>
    <div class="feed-foot">Friendbook Social Plugin</div>
  </aside>

  <footer class="footer">
    <div class="fcol" style="left:83px;width:110px"><h3>QUICK <span>LINKS</span></h3>
      <ul class="links"><li>Home</li><li>Event</li><li>Mt Corrie</li><li>Itinerary</li><li>Contact Us</li></ul></div>
    <span class="vsep" style="left:221px"></span>
    <div class="fcol contact" style="left:252px;width:206px"><h3>CONTACT <span>DETAILS</span></h3>
      <div class="name">Snowline SKI Challenge</div>
      <div class="addr">1234 Ridge Street, Alpine View,<br>Lakeside - 12345</div>
      <div class="row"><svg width="12" height="12" viewBox="0 0 12 12"><path d="M2 1l2 0 1 3-1.5 1a7 7 0 0 0 3.5 3.5L8 7l3 1v2l-1 1C5 11 1 7 1 2z" fill="#fff"/></svg>02 5550 1842</div>
      <div class="row"><svg width="12" height="12" viewBox="0 0 12 12"><rect x="3" y="1" width="6" height="3" fill="#fff"/><rect x="1" y="4" width="10" height="5" fill="#fff"/><rect x="3" y="8" width="6" height="3" fill="#fff" stroke="#1f1f1f"/></svg>02 5550 1842</div>
      <div class="row"><svg width="12" height="10" viewBox="0 0 12 10"><rect x="0" y="1" width="12" height="8" fill="#fff"/><path d="M0 1l6 4 6-4" fill="none" stroke="#1f1f1f"/></svg>enquiry@snowlineskichallenge.com.au</div>
    </div>
    <span class="vsep" style="left:485px"></span>
    <div class="fcol" style="left:516px;width:220px"><h3>QUICK <span>INQUIRY</span></h3>
      <div class="form"><div class="field">Name</div><div class="field">Email</div><div class="field msg">Message</div><div class="submit">SUBMIT</div></div></div>
    <span class="vsep" style="left:765px"></span>
    <div class="footer-brand">Snowline<br>SKI<br>Challenge</div>
  </footer>

  <div class="bottom"><span>Copyright © 2017 Snowline SKI Challenge. All Right Reserved.</span>
    <div class="social"><i></i><i></i><i></i><i></i></div></div>
</div>
</body>
</html>
```